Prairie Kettle Billboard

We are looking to have a new billboard design for our Casual Restaurant chain. We are a steakhouse chain that is very casual. You can visit our website at: www.prairiekettle-demo.net to get an idea of our menu. We are looking to have some new billboard ideas for our steakhouse so that we can communicate our concept to customers that are passing by the billboard. I have attached some items to give you a feel for our concept. The Billboard will be 14'X48'. I look forward to hearing from you. Glen

```html
<!DOCTYPE html>
<html lang="en">
<head>
<meta charset="utf-8">
<title>Prairie Kettle Billboard</title>
<link rel="stylesheet" href="https://fonts.googleapis.com/css2?family=Anton&family=Josefin+Sans:wght@700&display=swap">
<style>
  :root {
    --backdrop: #5a7ba6;
    --ember-dark: #3a0c06;
    --ember-mid: #8a1e0c;
    --ember-hot: #c8361a;
    --steak-light: #e8a35a;
    --steak-dark: #9a3a1c;
    --grill-red: #d8321c;
    --sign-fill: #5a0f0a;
    --sign-edge: #ff4a22;
    --name-gold: #ffc21a;
    --cream: #fff6e6;
  }
  html, body {
    margin: 0;
    padding: 0;
    width: 1200px;
    height: 1016px;
    overflow: hidden;
    background: var(--backdrop);
  }
  .canvas {
    position: relative;
    width: 1200px;
    height: 1016px;
  }
  .billboard {
    position: absolute;
    left: 40px;
    top: 372px;
    width: 1120px;
    height: 326px;
    background: linear-gradient(135deg, var(--ember-mid), var(--ember-dark) 55%, var(--ember-mid));
    box-shadow: 0 12px 30px rgba(0, 0, 0, 0.35);
  }
  .hero-photo {
    position: absolute;
    left: 0;
    top: 0;
    width: 500px;
    height: 100%;
    background:
      radial-gradient(ellipse 62% 40% at 48% 46%, var(--steak-light), var(--steak-dark) 70%, transparent 72%),
      linear-gradient(160deg, #2a0a06, var(--grill-red) 60%, #5a120a);
  }
  .ember-field {
    position: absolute;
    left: 500px;
    top: 0;
    right: 0;
    bottom: 0;
    background: radial-gradient(ellipse at 60% 40%, var(--ember-hot), var(--ember-mid) 50%, var(--ember-dark));
  }
  .brand-disc {
    position: absolute;
    left: 684px;
    top: -108px;
    width: 176px;
    height: 176px;
    border-radius: 50%;
    background: radial-gradient(circle at 40% 35%, #b82a18, var(--sign-fill));
    border: 4px solid var(--cream);
    box-sizing: border-box;
  }
  .name-plate {
    position: absolute;
    left: 544px;
    top: 36px;
    width: 544px;
    height: 170px;
    border-radius: 10px;
    background: var(--sign-fill);
    border: 3px solid var(--sign-edge);
    box-shadow: 0 0 18px rgba(255, 74, 34, 0.6);
    box-sizing: border-box;
    text-align: center;
  }
  .brand-name {
    margin: 44px 0 0;
    font-family: "Anton", "Impact", sans-serif;
    font-weight: 400;
    font-size: 76px;
    line-height: 1;
    color: var(--name-gold);
    letter-spacing: 1px;
    text-transform: uppercase;
  }
  .brand-subline {
    margin: 6px 0 0;
    font-family: "Josefin Sans", "Arial", sans-serif;
    font-weight: 700;
    font-size: 27px;
    color: var(--cream);
    letter-spacing: 2px;
    text-transform: uppercase;
  }
  .brand-subline .star { color: var(--name-gold); margin: 0 14px; }
  .headline {
    position: absolute;
    left: 500px;
    right: 0;
    top: 200px;
    margin: 0;
    text-align: center;
    font-family: "Anton", "Impact", sans-serif;
    font-weight: 400;
    font-size: 100px;
    line-height: 1.05;
    color: var(--cream);
    letter-spacing: 2px;
    text-transform: uppercase;
    text-shadow: 0 3px 8px rgba(0, 0, 0, 0.6);
  }
</style>
</head>
<body>
  <main class="canvas">
    <section class="billboard" aria-label="Prairie Kettle billboard">
      <div class="hero-photo" role="img" aria-label="Photo of a glazed grilled steak on a grill grate over glowing coals"></div>
      <div class="ember-field" role="img" aria-label="Photo of glowing red embers"></div>
      <div class="brand-disc" aria-hidden="true"></div>
      <div class="name-plate">
        <h1 class="brand-name">Prairie Kettle</h1>
        <p class="brand-subline"><span class="star">★★</span>Grill &amp; Saloon<span class="star">★★</span></p>
      </div>
      <p class="headline">Remarkable</p>
    </section>
  </main>
</body>
</html>
```